Creative Businesss Card desgin!

Create a business card for our business Gleam window cleaning!
We are open to creative ideas as long as it maintains a professional image.

Target Market(s)

Small Commercial window cleaning clients including car dealerships, strata manager, cafe

Industry/Entity Type

Window Cleaning

Contact Information for Business Card

Daniel Prescott
General Manager
Gleam Window Cleaning

daniel@gleamservices.com.au
pane-care-southbank.com.au
Ph: 1800 GET GLEAM
Mob: 0437 582 061

Colors
fbed22
0392cd

Requirements
Should not have
• Stock window cleaning/ squeegee graphics

```html
<!DOCTYPE html>
<html lang="en">
<head>
<meta charset="utf-8">
<title>Gleam Window Cleaning – Business Card</title>
<link href="https://fonts.googleapis.com/css2?family=Lato:wght@400;700;900&display=swap" rel="stylesheet">
<style>
  :root {
    --page-bg: #2b2b2b;
    --card-blue: #0b5585;
    --pattern-light: #2f6f9a;
    --pattern-dark: #0b5585;
    --gleam-yellow: #fbed22;
    --text-white: #ffffff;
  }
  * { margin: 0; padding: 0; box-sizing: border-box; }
  html, body {
    width: 1200px; height: 960px; overflow: hidden;
    background: var(--page-bg);
    font-family: "Lato", sans-serif;
  }
  .canvas { position: relative; width: 1200px; height: 960px; }
  .card {
    position: absolute; left: 281px; width: 654px; height: 372px;
    background: var(--card-blue); border-radius: 20px; overflow: hidden;
  }
  .card-front { top: 81px; }
  .card-back { top: 506px; }

  .holder { position: absolute; left: 62px; top: 107px; }
  .holder-name {
    color: var(--gleam-yellow); font-weight: 700; font-size: 24px; line-height: 1.1;
  }
  .holder-title {
    color: var(--text-white); font-size: 17px; margin-top: 6px;
  }
  .divider {
    position: absolute; left: 277px; top: 97px; width: 2px; height: 71px;
    background: var(--text-white);
  }
  .brand {
    position: absolute; left: 327px; top: 110px;
    display: flex; align-items: center; gap: 10px;
  }
  .brand-mark {
    width: 18px; height: 18px; border-radius: 50%; background: var(--gleam-yellow);
  }
  .brand-name {
    color: var(--gleam-yellow); font-weight: 900; font-size: 23px; line-height: 1.1;
    max-width: 230px;
  }
  .contacts { position: absolute; left: 332px; top: 201px; list-style: none; }
  .contact {
    display: flex; align-items: center; height: 22.3px;
    color: var(--text-white); font-size: 16px;
  }
  .contact-icon { width: 16px; height: 16px; margin-right: 9px; flex: none; }

  .pattern-field {
    position: absolute; left: 13px; top: 11px; width: 630px; height: 352px;
    border-radius: 14px;
    background: linear-gradient(160deg, var(--pattern-light), var(--pattern-dark));
    opacity: 0.7;
  }
  .back-brand {
    position: absolute; left: 96px; top: 175px;
    color: var(--gleam-yellow); font-weight: 900; font-size: 30px;
  }
</style>
</head>
<body>
<main class="canvas">
  <section class="card card-front" aria-label="Business card front">
    <div class="holder">
      <p class="holder-name">Daniel Prescott</p>
      <p class="holder-title">General Manager</p>
    </div>
    <div class="divider"></div>
    <div class="brand">
      <span class="brand-mark"></span>
      <span class="brand-name">Gleam Window Cleaning</span>
    </div>
    <ul class="contacts">
      <li class="contact">
        <svg class="contact-icon" viewBox="0 0 16 16"><path fill="#fbed22" d="M4 1 L7 4 L5 6.5 C6 9 7.5 10.5 9.5 11.5 L12 9.5 L15 12.5 L12.5 15 C6 14 2 10 1 3.5 Z"/></svg>
        1800 GET GLEAM
      </li>
      <li class="contact">
        <svg class="contact-icon" viewBox="0 0 16 16"><rect x="4" y="1" width="8" height="14" rx="1.5" fill="none" stroke="#fbed22" stroke-width="1.6"/><circle cx="8" cy="12.5" r="0.9" fill="#fbed22"/></svg>
        0437 582 061
      </li>
      <li class="contact">
        <svg class="contact-icon" viewBox="0 0 16 16"><rect x="1" y="3.5" width="14" height="9" fill="#fbed22"/><path d="M1 3.5 L8 9 L15 3.5" fill="none" stroke="#0b5585" stroke-width="1.2"/></svg>
        daniel@gleamservices.com.au
      </li>
      <li class="contact">
        <svg class="contact-icon" viewBox="0 0 16 16" fill="none" stroke="#fbed22" stroke-width="1.1"><circle cx="8" cy="8" r="6.5"/><ellipse cx="8" cy="8" rx="3" ry="6.5"/><path d="M1.5 8 H14.5 M2.5 4.8 H13.5 M2.5 11.2 H13.5"/></svg>
        pane-care-southbank.com.au
      </li>
    </ul>
  </section>

  <section class="card card-back" aria-label="Business card back">
    <div class="pattern-field" role="img" aria-label="Repeating faint brand pattern in soft blue tones"></div>
    <p class="back-brand">Gleam</p>
  </section>
</main>
</body>
</html>
```